Dalwick Self Storage Billboard

This is a 12'x24' billboard. I need this billboard to scream that it is for self storage with part of or all of the billboard having a picture of a storage unit or storage units in the background that matches my logo colors. You can use a stock image for this or I attached a picture if you would want to use that. I also need the billboard to include my logo which I have attached, the phone number of 555-014-2736, and I would like the billboard to say the following:
-Rent 100% Online at DalwickSelfStorage.example (emphasize this)
-Drive-Up & Temp-Controlled Units
-Covered & Uncovered Boat/RV Parking

I would also like there to be an arrow pointing LEFT on the bottom of the billboard that says: Millbrook Landing Apartments | 555-014-2981

```html
<!DOCTYPE html>
<html lang="en">
<head>
<meta charset="utf-8">
<title>Dalwick Self Storage Billboard</title>
<link href="https://fonts.googleapis.com/css2?family=Bebas+Neue&family=Poppins:wght@600;700&display=swap" rel="stylesheet">
<style>
  :root {
    --navy: #0c1d38;
    --navy-deep: #08152b;
    --brand-blue: #1b5ea8;
    --sky-blue: #2f7fd0;
    --teal: #2a8fa6;
    --teal-light: #4fb3c6;
    --ink: #0a0a0a;
    --white: #ffffff;
    --backdrop: #cbcbcb;
  }
  html, body {
    margin: 0;
    padding: 0;
    width: 837px;
    height: 1200px;
    overflow: hidden;
    background: var(--backdrop);
  }
  .billboard {
    position: absolute;
    left: 28px;
    top: 405px;
    width: 780px;
    height: 389px;
    box-shadow: 0 12px 28px rgba(0,0,0,0.35);
  }
  .billboard svg { display: block; width: 100%; height: 100%; }
  .title { font-family: 'Bebas Neue', sans-serif; font-size: 140px; }
  .rent-text { font-family: 'Bebas Neue', sans-serif; font-size: 62px; }
  .feature { font-family: 'Poppins', sans-serif; font-weight: 600; font-size: 28px; fill: var(--white); }
  .phone-number { font-family: 'Poppins', sans-serif; font-weight: 700; font-size: 98px; fill: var(--ink); }
  .brand-name { font-family: 'Poppins', sans-serif; font-weight: 700; font-size: 34px; fill: var(--brand-blue); }
  .direction { font-family: 'Poppins', sans-serif; font-weight: 700; font-size: 45px; fill: var(--white); }
</style>
</head>
<body>
<div class="billboard">
  <svg viewBox="0 0 1299 648" xmlns="http://www.w3.org/2000/svg">
    <defs>
      <linearGradient id="unitsTone" x1="0" y1="0" x2="1" y2="0">
        <stop offset="0" stop-color="#15334f"/>
        <stop offset="0.5" stop-color="#2a7f95"/>
        <stop offset="1" stop-color="#3aa6bd"/>
      </linearGradient>
      <linearGradient id="navyTone" x1="0" y1="0" x2="1" y2="1">
        <stop offset="0" stop-color="#0e2342"/>
        <stop offset="1" stop-color="#08152b"/>
      </linearGradient>
    </defs>

    <!-- dark header field -->
    <rect class="header-field" x="0" y="0" width="1299" height="400" fill="url(#navyTone)"/>

    <!-- storage units photo area -->
    <polygon class="units-photo" role="img" aria-label="Row of storage units with teal roll-up doors"
      points="900,0 1299,0 1299,540 1200,540 1050,395 880,395 880,120"
      fill="url(#unitsTone)"/>

    <!-- white contact field -->
    <polygon class="contact-field" points="0,395 1050,395 1200,532 1200,648 0,648" fill="var(--white)"/>
    <rect x="1200" y="532" width="99" height="116" fill="var(--white)"/>

    <!-- title -->
    <text class="title" x="45" y="165"><tspan fill="var(--white)">DALWICK </tspan><tspan fill="var(--sky-blue)">SELF STORAGE</tspan></text>

    <!-- rent online banner -->
    <rect x="45" y="185" width="250" height="85" rx="6" fill="var(--brand-blue)"/>
    <rect x="280" y="185" width="618" height="85" rx="6" fill="var(--white)"/>
    <text class="rent-text" x="62" y="250" fill="var(--white)">RENT 100%</text>
    <text class="rent-text" x="292" y="250" fill="var(--ink)" textLength="594" lengthAdjust="spacingAndGlyphs">ONLINE AT DALWICKSELFSTORAGE.EXAMPLE</text>

    <!-- feature: drive-up units -->
    <rect x="47" y="290" width="66" height="62" rx="6" fill="var(--brand-blue)"/>
    <path d="M64,332 a10,10 0 0 1 3,-19 a14,14 0 0 1 27,2 a9,9 0 0 1 1,17 z" fill="var(--white)"/>
    <path d="M80,337 v-14 M73,326 l7,-7 l7,7" stroke="var(--brand-blue)" stroke-width="4" fill="none" stroke-linecap="round"/>
    <text class="feature" x="133" y="315">Drive-Up &amp; Temp</text>
    <text class="feature" x="133" y="347">Controlled Units</text>

    <line x1="425" y1="295" x2="425" y2="368" stroke="#6f7f96" stroke-width="2"/>

    <!-- feature: boat/rv parking -->
    <rect x="466" y="297" width="66" height="62" rx="6" fill="var(--brand-blue)"/>
    <rect x="481" y="309" width="36" height="38" fill="none" stroke="var(--white)" stroke-width="3"/>
    <path d="M484,316 h30 M484,322 h30 M484,328 h30" stroke="var(--white)" stroke-width="2"/>
    <rect x="488" y="333" width="22" height="9" rx="2" fill="var(--white)"/>
    <text class="feature" x="551" y="322">Covered &amp; Uncovered</text>
    <text class="feature" x="551" y="354">Boat/RV Parking</text>

    <!-- phone -->
    <circle cx="89" cy="465" r="40" fill="var(--brand-blue)"/>
    <path d="M75,447 c-6,4 -6,14 2,25 c8,11 18,16 25,12 l4,-4 l-9,-9 l-5,4 c-4,-2 -9,-8 -11,-13 l4,-5 l-7,-10 z" fill="var(--white)"/>
    <path d="M92,446 a16,16 0 0 1 14,14 M92,437 a25,25 0 0 1 22,22" stroke="var(--white)" stroke-width="3" fill="none" stroke-linecap="round"/>
    <text class="phone-number" x="143" y="500">555-014-2736</text>

    <!-- brand name -->
    <rect x="848" y="432" width="44" height="44" fill="var(--navy)"/>
    <text class="brand-name" x="902" y="453">Dalwick</text>
    <text class="brand-name" x="902" y="490" style="font-size:26px">Self Storage</text>

    <!-- direction arrow -->
    <rect x="105" y="532" width="1194" height="86" fill="var(--brand-blue)"/>
    <polygon points="5,575 105,518 105,632" fill="var(--brand-blue)"/>
    <text class="direction" x="107" y="591">Millbrook Landing Apartments | 555-014-2981</text>
  </svg>
</div>
</body>
</html>
```